Kestrel Motorworks Card

Our company is an offroad fabrication shop that does everything from product installs to complete turnkey offroad racers. We are looking to generate new business cards for the 2014 Lords of the Canyon race in February. This is one of the largest offroad races in the country. We would like to see designs that incorporate the colors used in our logo - black, red, and white.

Industry/Entity Type

Shop

Contact Information for Business Card

KESTREL Motorworks, 2873 Marwood Ln. Houston, TX, 713-452-3071, www.kestrelmotorworks.example, Leon Farrowby, Owen Tilsley, Owners.

Requirements
Nice to have
• Would like to see the Logo full size on the back size of the car.

```html
<!DOCTYPE html>
<html lang="en">
<head>
<meta charset="utf-8">
<title>Kestrel Motorworks Business Card</title>
<link href="https://fonts.googleapis.com/css2?family=Arimo:wght@700&display=swap" rel="stylesheet">
<style>
  :root {
    --bg: #e2e2e2;
    --red: #e0231d;
    --black: #141414;
    --white: #ffffff;
    --ink: #1a1a1a;
  }
  * { box-sizing: border-box; margin: 0; padding: 0; }
  html, body { width: 1200px; height: 796px; overflow: hidden; }
  body {
    background: var(--bg);
    font-family: "Arimo", Arial, sans-serif;
    font-weight: 700;
    display: flex;
    align-items: center;
    justify-content: center;
    gap: 60px;
  }
  .card {
    position: relative;
    width: 520px;
    height: 298px;
    background: var(--white);
    overflow: hidden;
    box-shadow: 0 3px 10px rgba(0,0,0,0.25);
  }
  .card-bands {
    position: absolute;
    inset: 0;
    width: 100%;
    height: 100%;
  }
  .band-red { fill: var(--red); }
  .band-black { fill: var(--black); }

  /* Front */
  .brand-mark {
    position: absolute;
    left: 50%;
    top: 72px;
    transform: translateX(-50%);
    display: flex;
    align-items: center;
    gap: 12px;
    color: var(--red);
    font-size: 30px;
    white-space: nowrap;
  }
  .brand-mark-square {
    width: 26px;
    height: 26px;
    background: var(--red);
  }
  .brand-name {
    position: absolute;
    left: 0;
    right: 0;
    top: 150px;
    text-align: center;
    color: var(--red);
    font-size: 30px;
    white-space: nowrap;
  }

  /* Back */
  .name-tag {
    position: absolute;
    right: 0;
    top: 92px;
    background: var(--red);
    color: var(--white);
    font-size: 19px;
    padding: 4px 22px 4px 20px;
    border-radius: 14px 0 0 14px;
  }
  .icon-strip {
    position: absolute;
    left: 0;
    top: 80px;
    width: 32px;
    height: 100px;
    background: var(--black);
    display: flex;
    flex-direction: column;
    align-items: center;
    justify-content: space-around;
    padding: 8px 0;
  }
  .icon-strip svg { width: 14px; height: 14px; fill: var(--red); }
  .contact-list {
    position: absolute;
    left: 46px;
    top: 100px;
    list-style: none;
    color: var(--ink);
    font-size: 16px;
    line-height: 26px;
  }
</style>
</head>
<body>

  <section class="card card-front" aria-label="Business card front">
    <svg class="card-bands" viewBox="0 0 520 298" preserveAspectRatio="none" aria-hidden="true">
      <path class="band-black" d="M0,0 H520 V40 C360,14 170,24 0,64 Z"/>
      <path class="band-red" d="M0,0 H520 V14 C350,2 160,20 0,58 Z"/>
      <path class="band-black" d="M0,298 V210 C160,252 360,280 520,266 V298 Z"/>
      <path class="band-red" d="M0,298 V240 C160,272 360,290 520,284 V298 Z"/>
    </svg>
    <div class="brand-mark">
      <span class="brand-mark-square"></span>
      <span>Kestrel Motorworks</span>
    </div>
    <h1 class="brand-name">KESTREL Motorworks</h1>
  </section>

  <section class="card card-back" aria-label="Business card back">
    <svg class="card-bands" viewBox="0 0 520 298" preserveAspectRatio="none" aria-hidden="true">
      <path class="band-black" d="M0,0 H520 V70 C380,30 180,30 0,40 Z"/>
      <path class="band-red" d="M0,0 H520 V50 C380,16 180,18 0,26 Z"/>
      <path class="band-black" d="M0,298 V200 C140,240 340,250 520,232 V298 Z"/>
      <path class="band-red" d="M0,298 V250 C150,272 340,276 520,262 V298 Z"/>
    </svg>
    <div class="name-tag">Owen Tilsley</div>
    <div class="icon-strip" aria-hidden="true">
      <svg viewBox="0 0 24 24"><path d="M12 2C8 2 5 5 5 9c0 5 7 13 7 13s7-8 7-13c0-4-3-7-7-7zm0 10a3 3 0 1 1 0-6 3 3 0 0 1 0 6z"/></svg>
      <svg viewBox="0 0 24 24"><path d="M6.6 10.8a15 15 0 0 0 6.6 6.6l2.2-2.2c.3-.3.7-.4 1-.2 1.1.4 2.3.6 3.6.6.6 0 1 .4 1 1V20c0 .6-.4 1-1 1A17 17 0 0 1 3 4c0-.6.4-1 1-1h3.5c.6 0 1 .4 1 1 0 1.3.2 2.5.6 3.6.1.3 0 .7-.2 1z"/></svg>
      <svg viewBox="0 0 24 24"><path d="M12 2a10 10 0 1 0 0 20 10 10 0 0 0 0-20zm6.9 6h-3a15 15 0 0 0-1.3-3.9A8 8 0 0 1 18.9 8zM12 4c.8 1.2 1.5 2.5 1.9 4h-3.8c.4-1.5 1.1-2.8 1.9-4zM4.3 14a8 8 0 0 1 0-4h3.4a16 16 0 0 0 0 4zm.8 2h3a15 15 0 0 0 1.3 3.9A8 8 0 0 1 5.1 16zm3-8h-3a8 8 0 0 1 4.3-3.9C8.8 5.3 8.4 6.6 8.1 8zM12 20c-.8-1.2-1.5-2.5-1.9-4h3.8c-.4 1.5-1.1 2.8-1.9 4zm2.3-6H9.7a14 14 0 0 1 0-4h4.6a14 14 0 0 1 0 4zm.3 5.9c.6-1.2 1-2.5 1.3-3.9h3a8 8 0 0 1-4.3 3.9zm1.7-5.9a16 16 0 0 0 0-4h3.4a8 8 0 0 1 0 4z"/></svg>
    </div>
    <ul class="contact-list">
      <li class="contact-address">2873 Marwood Ln. Houston, TX</li>
      <li class="contact-phone">713-452-3071</li>
      <li class="contact-web">www.kestrelmotorworks.example</li>
    </ul>
  </section>

</body>
</html>
```